Adult Residential Care Provider (Assisted Living) needs a brochure design.

We need a brochure designed for our assisted living facilites in Metairie (adjacent to New Orleans) called Willowmere Elder Homes. We provide adults, typically Seniors, a place to live where they receive 24-hour care/support of their daily living activities, including laundering, cooking, cleaning, grooming, bathing, etc.. I'd like to use our logo and the color choices should be soft and convey comfort. I would also like the brochure to be editable by my administration to make any changes in the future.

```html
<!DOCTYPE html>
<html lang="en">
<head>
<meta charset="utf-8">
<title>Willowmere Elder Homes – Assisted Living Flyer</title>
<link href="https://fonts.googleapis.com/css2?family=Montserrat:wght@400;500;600;700;800&display=swap" rel="stylesheet">
<style>
:root{
  --teal:#0f7d6e;
  --teal-dark:#0b5e53;
  --teal-deep:#0a4f46;
  --teal-light:#16a594;
  --cream:#f3ede2;
  --beige:#efe3c4;
  --ink:#2b3a38;
  --white:#ffffff;
  --pill-text:#e6f4ee;
}
*{margin:0;padding:0;box-sizing:border-box}
html,body{width:720px;height:1200px;overflow:hidden;background:var(--white)}
body{font-family:'Montserrat',sans-serif;color:var(--ink)}
.flyer{position:relative;width:720px;height:1200px;overflow:hidden;background:var(--white)}
.flyer__art{position:absolute;inset:0}
.brand{position:absolute;left:28px;top:24px;display:flex;align-items:center;gap:12px}
.brand__dot{width:40px;height:40px;border-radius:50%;background:var(--teal)}
.brand__name{font-family:'Montserrat',sans-serif;font-weight:600;color:var(--teal-dark);font-size:20px;line-height:1.15;letter-spacing:1.5px;text-transform:uppercase}
.headline{position:absolute;left:28px;top:108px;font-weight:800;font-size:45px;line-height:50px;color:var(--teal-dark);letter-spacing:.5px}
.headline__rule{position:absolute;left:28px;top:322px;width:278px;height:2px;background:var(--teal-dark)}
.headline__site{position:absolute;left:28px;top:334px;font-weight:600;font-size:19px;letter-spacing:1.4px;color:var(--teal-dark)}
.services-tab{position:absolute;left:212px;top:614px;width:194px;height:62px;border-radius:22px;background:var(--teal);color:var(--white);font-weight:700;font-size:26px;letter-spacing:1px;display:flex;align-items:center;justify-content:center}
.services{position:absolute;top:698px;list-style:none;font-size:17px;line-height:24px}
.services--left{left:48px;width:270px}
.services--right{left:338px;width:340px}
.services li{position:relative;padding-left:28px}
.services li::before{content:"";position:absolute;left:0;top:4px;width:16px;height:16px;border-radius:50%;background:var(--teal)}
.services li::after{content:"";position:absolute;left:5px;top:7px;width:4px;height:7px;border:solid var(--white);border-width:0 2px 2px 0;transform:rotate(45deg)}
.facilities{position:absolute;left:75px;top:878px;width:572px;height:42px;border-radius:21px;background:var(--teal);box-shadow:0 2px 0 var(--teal-deep);color:var(--pill-text);font-weight:600;font-size:20px;display:flex;align-items:center;justify-content:center}
.amenities{position:absolute;left:0;top:940px;width:720px;height:80px}
.details{position:absolute;left:0;top:1038px;width:720px;text-align:center;font-weight:600;font-size:18px;color:var(--teal-dark)}
.footer{position:absolute;left:0;top:1100px;width:720px;height:100px;background:var(--teal)}
.footer__addresses{position:absolute;left:0;top:30px;width:720px;display:flex;justify-content:center;gap:26px;color:var(--white);font-size:14px}
.footer__addr{display:flex;align-items:center;gap:10px}
.footer__site{position:absolute;left:0;bottom:0;width:720px;height:34px;background:var(--teal-dark);color:var(--white);font-size:11px;letter-spacing:5px;display:flex;align-items:center;justify-content:center}
.call{position:absolute;left:180px;top:1074px;width:364px;height:42px;border-radius:21px;background:var(--beige);display:flex;align-items:center;justify-content:center;gap:10px;font-weight:600;font-size:20px;color:var(--teal-dark);letter-spacing:.5px}
</style>
</head>
<body>
<div class="flyer">
  <svg class="flyer__art" width="720" height="1200" viewBox="0 0 720 1200" aria-hidden="false">
    <defs>
      <linearGradient id="tealSweep" x1="0" y1="0" x2="1" y2="1">
        <stop offset="0" stop-color="#1aa898"/>
        <stop offset="1" stop-color="#0b5e53"/>
      </linearGradient>
      <radialGradient id="photoTone" cx="0.6" cy="0.45" r="0.7">
        <stop offset="0" stop-color="#e9d2b4"/>
        <stop offset="0.6" stop-color="#c9a27a"/>
        <stop offset="1" stop-color="#f4ece0"/>
      </radialGradient>
      <radialGradient id="handsTone" cx="0.5" cy="0.5" r="0.6">
        <stop offset="0" stop-color="#c98b58"/>
        <stop offset="1" stop-color="#e8b27a"/>
      </radialGradient>
    </defs>
    <rect class="bg-cream" x="0" y="0" width="720" height="680" fill="var(--cream)"/>
    <path class="sweep-teal" d="M0 400 C50 530 170 585 300 592 C430 598 570 590 720 528 L720 680 L0 680 Z" fill="url(#tealSweep)"/>
    <path class="sweep-accent" d="M0 430 C60 540 170 578 300 584" fill="none" stroke="#0a4f46" stroke-width="4" opacity=".5"/>
    <path class="photo-band" d="M268 545 C298 290 490 92 720 70 L720 575 C600 615 430 605 268 545 Z" fill="var(--teal)"/>
    <path class="photo-frame" d="M292 528 C322 305 500 122 720 104 L720 548 C600 586 445 576 292 528 Z" fill="var(--white)"/>
    <path class="photo" role="img" aria-label="Photo: a caregiver smiling with an elderly resident" d="M300 522 C330 310 505 130 720 112 L720 540 C600 578 450 568 300 522 Z" fill="url(#photoTone)"/>
    <circle class="hands-ring" cx="310" cy="552" r="100" fill="var(--teal)"/>
    <circle class="hands-frame" cx="310" cy="552" r="91" fill="var(--white)"/>
    <circle class="hands-photo" role="img" aria-label="Photo: two hands holding each other" cx="310" cy="552" r="86" fill="url(#handsTone)"/>
    <rect x="0" y="680" width="720" height="420" fill="var(--white)"/>
  </svg>

  <div class="brand">
    <span class="brand__dot"></span>
    <div class="brand__name">Willowmere<br>Elder Homes</div>
  </div>

  <h1 class="headline">ASSISTED<br>LIVING &amp;<br>RESIDENTIAL<br>CARE</h1>
  <div class="headline__rule"></div>
  <div class="headline__site">www.willowmerehomes.com</div>

  <div class="services-tab">SERVICES</div>

  <ul class="services services--left">
    <li>24 Hours Care</li>
    <li>Assistance with Daily Living Activities</li>
    <li>Bathing Assistance</li>
    <li>Beauty and Haircare</li>
    <li>Laundry</li>
  </ul>
  <ul class="services services--right">
    <li>Housekeeping</li>
    <li>3 Home-Cooked Meals and Snacks - Dietitian Approved</li>
    <li>Medication Reminders and Supervision</li>
  </ul>

  <div class="facilities">Accommodation | Laundry | Food | Medication Storage</div>

  <svg class="amenities" viewBox="0 0 720 80" fill="none" stroke="var(--teal-dark)" stroke-width="2.5" stroke-linecap="round" stroke-linejoin="round">
    <g class="amenity amenity--care" transform="translate(157 40)">
      <circle r="34" fill="var(--white)" stroke="#cfd8d6" stroke-width="3"/>
      <circle r="28" stroke="var(--teal)"/>
      <path d="M0 6 C-12 -3 -12 -14 -5 -14 C-2 -14 0 -11 0 -9 C0 -11 2 -14 5 -14 C12 -14 12 -3 0 6 Z" fill="var(--teal)" stroke="none"/>
      <path d="M-16 2 L-10 14 L4 14 M16 2 L10 14"/>
    </g>
    <g class="amenity amenity--bath" transform="translate(259 40)">
      <circle r="34" fill="var(--white)" stroke="#cfd8d6" stroke-width="3"/>
      <circle r="28" stroke="var(--teal)"/>
      <path d="M-10 14 L-10 -4 C-10 -12 0 -14 4 -8"/>
      <path d="M0 -8 L10 -8" stroke-width="4"/>
      <path d="M3 -2 L1 4 M7 -2 L7 4 M11 -2 L13 4"/>
    </g>
    <g class="amenity amenity--food" transform="translate(361 40)">
      <circle r="34" fill="var(--white)" stroke="#cfd8d6" stroke-width="3"/>
      <circle r="28" stroke="var(--teal)"/>
      <path d="M-15 0 L15 0 C15 10 7 14 0 14 C-7 14 -15 10 -15 0 Z"/>
      <path d="M-5 -6 C-8 -10 -2 -12 -5 -16 M1 -6 C-2 -10 4 -12 1 -16 M7 -6 C4 -10 10 -12 7 -16"/>
    </g>
    <g class="amenity amenity--laundry" transform="translate(463 40)">
      <circle r="34" fill="var(--white)" stroke="#cfd8d6" stroke-width="3"/>
      <circle r="28" stroke="var(--teal)"/>
      <rect x="-13" y="-15" width="26" height="30" rx="3"/>
      <path d="M-13 -8 L13 -8"/>
      <circle cx="0" cy="4" r="7"/>
    </g>
    <g class="amenity amenity--hair" transform="translate(566 40)">
      <circle r="34" fill="var(--white)" stroke="#cfd8d6" stroke-width="3"/>
      <circle r="28" stroke="var(--teal)"/>
      <circle cx="-8" cy="9" r="4.5"/>
      <circle cx="8" cy="9" r="4.5"/>
      <path d="M-5 5 L10 -14 M5 5 L-10 -14"/>
    </g>
  </svg>

  <div class="details">FOR FURTHER DETAILS</div>

  <div class="footer">
    <div class="footer__addresses">
      <span class="footer__addr">
        <svg width="26" height="26" viewBox="0 0 26 26" fill="none" stroke="#fff" stroke-width="1.5"><circle cx="13" cy="13" r="12"/><path d="M13 20 C9 15 8 13 8 11 A5 5 0 0 1 18 11 C18 13 17 15 13 20 Z"/><circle cx="13" cy="11" r="1.8"/></svg>
        240 Linden Ave. Metairie, LA 70005
      </span>
      <span class="footer__addr">
        <svg width="26" height="26" viewBox="0 0 26 26" fill="none" stroke="#fff" stroke-width="1.5"><circle cx="13" cy="13" r="12"/><path d="M13 20 C9 15 8 13 8 11 A5 5 0 0 1 18 11 C18 13 17 15 13 20 Z"/><circle cx="13" cy="11" r="1.8"/></svg>
        1512 Harbor Glen St. Metairie, LA 70002
      </span>
    </div>
    <div class="footer__site">WWW.WILLOWMEREHOMES.COM</div>
  </div>

  <div class="call">
    <span>CALL US ON</span>
    <svg width="26" height="26" viewBox="0 0 26 26"><circle cx="13" cy="13" r="12" fill="var(--teal-dark)"/><path d="M9 7 L11 7 L12 10 L10.5 11.5 C11.3 13.2 12.8 14.7 14.5 15.5 L16 14 L19 15 L19 17 C19 18 18 19 17 19 C12 18.5 7.5 14 7 9 C7 8 8 7 9 7 Z" fill="var(--beige)"/></svg>
    <span>(504) 555-0148</span>
  </div>
</div>
</body>
</html>
```